Coffee Beans Packaging

We are a coffee distribution company that imports coffee beans from around the world. Our coffee beans will be packaged in kraft (brown paper) packaging and we would like to have a slip on wrap around the kraft pack (can be positioned horizontally/vertically).

Some of the countries that are importing the coffee beans include Costa Rica, Dominican Republic, Honduras Coffee. We would like to include pictures that symbolize these countries of origins on our packaging as well.

Logo: We do not have a logo at the moment but you can add "Bean Harbor" as our brand name in your designs.

Colour Scheme: Vibrant colours but still relatable to coffee

Pictures: Please take a look at the attached files for inspiration/ adapt the designs to the packaging.

Target Market(s)

Coffee lovers, early twenties - late thirties

Industry/Entity Type

It Company

Requirements
Must have
• Pictures depicting the countries of origins

```html
<!DOCTYPE html>
<html lang="en">
<head>
<meta charset="utf-8">
<title>Bean Harbor – Coffee Wrap Label</title>
<link rel="stylesheet" href="https://fonts.googleapis.com/css2?family=Pinyon+Script&family=Playfair+Display:wght@400&family=Source+Sans+3:wght@400;600&display=swap">
<style>
  :root {
    --leaf: #8dc63f;
    --leaf-line: #a9d46a;
    --leaf-pale: #eef7e0;
    --sun: #ffdd15;
    --paper: #ffffff;
    --ink-light: #ffffff;
    --bean-dark: #6b4a2e;
    --bean-mid: #a0703f;
    --sea: #5aa6c8;
  }
  * { margin: 0; padding: 0; box-sizing: border-box; }
  html, body { width: 1200px; height: 508px; overflow: hidden; background: var(--paper); }
  .wrap-label { position: relative; width: 1200px; height: 508px; }

  /* Front badge */
  .badge-band {
    position: absolute; left: 0; top: 172px; width: 418px; height: 185px;
    background: var(--sun); border-radius: 0 12px 12px 0;
  }
  .badge-frame { position: absolute; left: 0; top: 0; width: 418px; height: 508px; }
  .origin-pictures {
    position: absolute; left: 0; width: 418px; top: 62px;
    display: flex; justify-content: center; gap: 12px;
  }
  .origin-picture { width: 28px; height: 28px; border-radius: 50%; }
  .origin-picture--costa-rica { background: linear-gradient(135deg, var(--leaf), var(--bean-dark)); }
  .origin-picture--dominican { background: linear-gradient(135deg, var(--sea), var(--bean-mid)); }
  .origin-picture--honduras { background: linear-gradient(135deg, var(--bean-mid), var(--leaf)); }
  .badge-tagline {
    position: absolute; left: 0; width: 418px; top: 106px; text-align: center;
    font-family: "Pinyon Script", cursive; font-size: 30px; line-height: 40px; color: var(--leaf);
  }
  .badge-brand {
    position: absolute; left: 0; width: 418px; top: 234px; text-align: center;
    font-family: "Playfair Display", serif; font-weight: 400; font-size: 64px; line-height: 68px;
    color: var(--leaf); transform: scaleX(0.66); white-space: nowrap;
  }
  .badge-claim {
    position: absolute; left: 0; width: 418px; top: 391px; text-align: center;
    font-family: "Source Sans 3", sans-serif; font-size: 13px; letter-spacing: 0.5px;
    color: var(--leaf);
  }

  /* Back panel */
  .info-panel {
    position: absolute; left: 418px; top: 89px; width: 782px; height: 361px;
    background: var(--leaf); border-radius: 12px; border: 2px solid var(--leaf-line);
  }
  .info-panel::before, .info-panel::after {
    content: ""; position: absolute; border: 1px solid rgba(255,255,255,0.75); border-radius: 8px;
  }
  .info-panel::before { inset: 8px; }
  .info-panel::after { inset: 13px; }
  .info-story {
    position: absolute; left: 20px; right: 20px; top: 36px; text-align: center;
    font-family: "Pinyon Script", cursive; font-size: 22px; line-height: 46px;
    color: var(--ink-light); white-space: nowrap;
  }
  .info-story .brand-quote {
    display: inline-block; font-family: "Playfair Display", serif; font-size: 26px;
    transform: scaleX(0.72); margin: 0 -14px;
  }
  .info-flourish {
    position: absolute; left: 296px; top: 140px; width: 185px; height: 18px;
    background: var(--sun); border-radius: 9px; opacity: 0.85;
  }
  .info-storage {
    position: absolute; left: 70px; width: 320px; top: 192px; text-align: center;
    font-family: "Source Sans 3", sans-serif; font-weight: 600; font-size: 15px;
    color: var(--ink-light);
  }
  .icon-dispose {
    position: absolute; left: 155px; top: 248px; width: 36px; height: 46px;
    background: var(--ink-light); border-radius: 3px 3px 7px 7px;
  }
  .icon-recycle { position: absolute; left: 241px; top: 242px; width: 56px; height: 56px; }
  .info-divider {
    position: absolute; left: 386px; top: 191px; width: 1.5px; height: 101px;
    background: var(--ink-light);
  }
  .info-process {
    position: absolute; left: 402px; width: 360px; top: 187px; text-align: center;
    font-family: "Source Sans 3", sans-serif; font-size: 15px; line-height: 21px;
    color: var(--ink-light); white-space: nowrap;
  }
</style>
</head>
<body>
<main class="wrap-label">
  <section class="badge">
    <div class="badge-band"></div>
    <svg class="badge-frame" viewBox="0 0 418 508" role="img" aria-label="Ornate scrolled label frame in green line work">
      <defs>
        <linearGradient id="frame-fill" x1="0" y1="0" x2="0" y2="1">
          <stop offset="0" stop-color="#eef7e0"/>
          <stop offset="0.5" stop-color="#ffffff"/>
          <stop offset="1" stop-color="#eef7e0"/>
        </linearGradient>
      </defs>
      <path fill="url(#frame-fill)"
        d="M209 500 C160 470 100 450 40 440 C30 400 55 380 45 350 L20 350 C5 320 5 200 20 170 L45 170 C55 140 30 110 40 75 C95 70 140 60 170 40 C185 20 195 10 209 8 C223 10 233 20 248 40 C278 60 323 70 378 75 C388 110 363 140 373 170 L398 170 C413 200 413 320 398 350 L373 350 C363 380 388 400 378 440 C318 450 258 470 209 500 Z"/>
    </svg>
    <div class="origin-pictures">
      <div class="origin-picture origin-picture--costa-rica" role="img" aria-label="Costa Rica coffee highlands picture"></div>
      <div class="origin-picture origin-picture--dominican" role="img" aria-label="Dominican Republic coast and coffee picture"></div>
      <div class="origin-picture origin-picture--honduras" role="img" aria-label="Honduras mountain coffee farm picture"></div>
    </div>
    <p class="badge-tagline">Finest Quality</p>
    <h1 class="badge-brand">Bean Harbor</h1>
    <p class="badge-claim">FRESH &amp; NATURAL</p>
  </section>

  <section class="info-panel">
    <p class="info-story">Carefully harvested and only the freshest &amp; finest beans are selected to capture<br>that taste and aroma which gives you the perfect <span class="brand-quote">“Bean Harbor”</span> feel in every sip.</p>
    <div class="info-flourish" role="img" aria-label="Decorative yellow scroll flourish"></div>
    <p class="info-storage">Store in a cool dry place.</p>
    <div class="icon-dispose" role="img" aria-label="Dispose of packaging in a bin symbol"></div>
    <svg class="icon-recycle" viewBox="0 0 56 56" aria-label="Recycle symbol" role="img">
      <g fill="none" stroke="#ffffff" stroke-width="5" stroke-linecap="round">
        <path d="M14 20 A18 18 0 0 1 38 10"/>
        <path d="M47 24 A18 18 0 0 1 36 46"/>
        <path d="M24 47 A18 18 0 0 1 9 30"/>
      </g>
      <g fill="#ffffff">
        <path d="M36 3 L46 12 L33 16 Z"/>
        <path d="M43 49 L30 51 L35 40 Z"/>
        <path d="M3 28 L14 24 L13 37 Z"/>
      </g>
    </svg>
    <div class="info-divider"></div>
    <p class="info-process">Bean Harbor uses latest technology and<br>techniques to enhance the natural coffee<br>essence &amp; aroma to develop a finest blend.<br>The result is a revitalizing effect which is<br>experienced &amp; enjoyed in every sip.</p>
  </section>
</main>
</body>
</html>
```